Australian Consultant Pharmacist Business Needs A3 Flyer for Medical Centre

Our business has just secured a deal in a medical centre to offer our consulting services. We have installed our software on the doctors computers and would like to have an A3 flyer to put on their walls to remind them about our services and explain very briefly how to use our simple software.

We would like the flyer to be vibrant and very simple whilst conveying our message of improving patient health outcomes and illustrating how to use our software and service.

We provide Home Medicine Reviews (HMR) for General Practitioners (GP) at medical centres.

There are 3 pathways for a GP to use our service, all resulting in the same outcome.

The outcome is the Dr sends us a referral for a HMR for their patient. In turn they receive a report back after we have performed the HMR.

Pathways
1.
-GP Opens Patient File in medical prescribing software
-If patient is eligible for a HMR, an alert will pop up in bottom right hand corner (approx 30 seconds)
- Click Send Referral
- New page opens, select reason for referral ie. several medicines
- Press Send - referral is sent electronically to Pharmacist

2.
No alert pops up but GP still wants to refer.
Right click RX Notify program - RX Notify program is identified by the bell shape icon in the bottom right side of the desktop tray next to the time.
Click refer current patient - this will refer the patient currently open on the GP prescribing software

3. GP would like to send HMR Referal via Fax.
Fax number 03 9172 3408

I have attached some examples of how the software and service works, including screen shots and some power points. I would like to use these as ideas for our A3 Flyer.

Good Luck!

Target Market(s)

Doctors

Industry/Entity Type

Health Service

Colors
f37122
0455a3
3176b5
33a6d7
f68d4c

Requirements
Must have
• Our company name - Brightpath Care HMR
• Our email brightpathcarehmr@mailvista.example
• our fax number
• the 3 ways to use our service and how
• prefer images and short keyword descriptions
• convey idea of improving patient health
• ensure our service comes accross as simple and effecient
Nice to have
• images, vibrant,
Should not have
• lengthy descriptions

```html
<!DOCTYPE html>
<html lang="en">
<head>
<meta charset="utf-8">
<title>Brightpath Care HMR – How to Refer a Patient</title>
<link rel="stylesheet" href="https://fonts.googleapis.com/css2?family=Crimson+Text:wght@400;600&family=Arimo:wght@400;700&display=swap">
<style>
  :root {
    --blue-deep: #0455a3;
    --blue-mid: #3176b5;
    --blue-sky: #33a6d7;
    --orange: #f37122;
    --orange-soft: #f68d4c;
    --paper: #ffffff;
    --ink: #3a3d44;
  }
  * { box-sizing: border-box; margin: 0; padding: 0; }
  html, body { width: 1200px; height: 799px; overflow: hidden; background: var(--paper); }
  .flyer { position: relative; width: 1200px; height: 799px; overflow: hidden; background: linear-gradient(180deg, #ffffff 0%, #f4f7fb 100%); font-family: "Arimo", Arial, sans-serif; color: var(--ink); }

  .hero-photo { position: absolute; left: 470px; top: 0; width: 730px; height: 340px;
    background: linear-gradient(100deg, rgba(255,255,255,1) 0%, rgba(222,231,240,0.9) 30%, #c9d6e3 60%, #dde6ef 100%); }
  .pills-photo { position: absolute; left: 880px; top: 230px; width: 220px; height: 100px; border-radius: 50%;
    background: radial-gradient(ellipse at center, #f0a15e 0%, #e6c3a0 45%, #d7e4ef 80%, rgba(255,255,255,0) 100%); }

  .brand { position: absolute; left: 56px; top: 228px; font-family: "Crimson Text", Georgia, serif; color: var(--blue-mid); }
  .brand-name { font-size: 56px; font-weight: 400; line-height: 1; }
  .brand-tagline { font-size: 28px; font-weight: 400; margin-left: 150px; margin-top: 2px; }

  .ribbon { position: absolute; left: 0; top: 336px; width: 760px; height: 52px; background: linear-gradient(90deg, var(--blue-deep), var(--blue-mid));
    color: #fff; font-family: "Crimson Text", Georgia, serif; font-weight: 600; font-size: 26px; line-height: 52px; padding-left: 56px; white-space: nowrap; }

  .pathway { position: absolute; border: 2px solid var(--blue-mid); border-radius: 10px; background: var(--paper); }
  .pathway-tab { position: absolute; top: -18px; left: -2px; background: var(--blue-mid); color: #fff; font-family: "Crimson Text", Georgia, serif;
    font-weight: 600; font-size: 20px; padding: 4px 16px; border-radius: 3px; white-space: nowrap; }
  .pathway-tab::before { content: ""; position: absolute; left: 40px; bottom: 100%; width: 2px; height: 22px; background: var(--blue-mid); }

  .steps { position: absolute; list-style: none; font-size: 12.5px; font-weight: 700; line-height: 1.3; color: var(--ink); }
  .steps li { position: relative; padding-left: 16px; margin-bottom: 9px; }
  .steps li:last-child { margin-bottom: 0; }
  .steps li::before { content: ""; position: absolute; left: 0; top: 5px; width: 7px; height: 7px; border-radius: 50%; background: var(--blue-sky); }
  .fax-number { color: var(--blue-deep); font-size: 14px; }

  .screen-shot { position: absolute; border: 2px solid var(--blue-mid); border-radius: 6px; background: linear-gradient(180deg, #eef2f7 0%, #d3dde8 100%); }
  .screen-label { position: absolute; left: 10px; top: 8px; font-size: 11px; font-weight: 700; color: var(--orange); }
  .screen-arrow { position: absolute; left: 30px; top: 22px; }

  .auto { left: 40px; top: 440px; width: 420px; height: 280px; }
  .auto .steps { left: 200px; top: 24px; width: 205px; }
  .manual { left: 480px; top: 420px; width: 350px; height: 275px; }
  .manual .steps { left: 154px; top: 24px; width: 186px; }
  .fax { left: 855px; top: 410px; width: 305px; height: 150px; }
  .fax .steps { left: 146px; top: 26px; width: 150px; }
  .fax-photo { position: absolute; left: 14px; top: 30px; width: 120px; height: 100px; border-radius: 8px; background: linear-gradient(160deg, #d9b8a0 0%, #6e6058 55%, #2d2d30 100%); }

  .footer { position: absolute; left: 0; bottom: 0; width: 1200px; height: 58px; background: linear-gradient(90deg, var(--blue-deep), var(--blue-mid));
    color: #fff; font-family: "Crimson Text", Georgia, serif; font-size: 22px; line-height: 58px; text-align: center; }
</style>
</head>
<body>
<main class="flyer">
  <div class="hero-photo" role="img" aria-label="Pharmacist talking with an older patient in a pharmacy"></div>
  <div class="pills-photo" role="img" aria-label="Colourful pills spilling from a glass jar"></div>

  <header class="brand">
    <h1 class="brand-name">Brightpath Care HMR</h1>
    <p class="brand-tagline">Improving Patient Outcomes</p>
  </header>

  <h2 class="ribbon">How to Refer a Patient for a Home Medicine Review (HMR)</h2>

  <section class="pathway auto">
    <h3 class="pathway-tab">Automatic Referral</h3>
    <div class="screen-shot" style="left:12px;top:28px;width:140px;height:64px;" role="img" aria-label="Desktop tray with RX Notify alert">
      <span class="screen-label">RX Notify program</span>
      <svg class="screen-arrow" width="60" height="30" viewBox="0 0 60 30"><path d="M2 4 L48 24" stroke="#f37122" stroke-width="4"/><path d="M40 26 L56 28 L48 14 Z" fill="#f37122"/></svg>
    </div>
    <div class="screen-shot" style="left:26px;top:102px;width:140px;height:72px;" role="img" aria-label="Referral alert pop-up window"></div>
    <div class="screen-shot" style="left:40px;top:184px;width:140px;height:80px;" role="img" aria-label="Referral reason selection page"></div>
    <ul class="steps">
      <li>GP Opens Patient File in medical prescribing software</li>
      <li>If patient is eligible for a HMR, an alert will pop up in bottom right hand corner (approx 30 seconds)</li>
      <li>Click Send Referral</li>
      <li>New page opens, select reason for referral ie. several medicines</li>
      <li>Press Send - referral is sent electronically to Pharmacist</li>
    </ul>
  </section>

  <section class="pathway manual">
    <h3 class="pathway-tab">Manual Referral</h3>
    <div class="screen-shot" style="left:12px;top:100px;width:130px;height:150px;" role="img" aria-label="Right-click menu on RX Notify bell icon in desktop tray"></div>
    <ul class="steps">
      <li>No alert pops up but GP still wants to refer.</li>
      <li>Right click RX Notify program - RX Notify program is identified by the bell shape icon in the bottom right side of the desktop tray next to the time.</li>
      <li>Click refer current patient - this will refer the patient currently open on the GP prescribing software</li>
    </ul>
  </section>

  <section class="pathway fax">
    <h3 class="pathway-tab">Fax Referral</h3>
    <div class="fax-photo" role="img" aria-label="Hand feeding a page into a fax machine"></div>
    <ul class="steps">
      <li>GP would like to send HMR Referral via Fax.</li>
      <li>Fax number<br><span class="fax-number">03 9172 3408</span></li>
    </ul>
  </section>

  <footer class="footer">For any assistance send us a mail at brightpathcarehmr@mailvista.example</footer>
</main>
</body>
</html>
```